Redesign Website - Current one too plain

The description is in the uploaded file. Please let me know if you need any more information. I'd prefer it if someone could implement the design to a WordPress site but the best design will win, regardless.
I would like the forms to look nice as well
UPDATE:
I don't think we can use the images that I provided, I think they make the site look a bit 'cheap' and I really don't know how to replace them. One thought I have had is to make the "Simple, Unique, Effective" a second feature on the right side of the page with the search on the left
Target Market(s)
Small companies, private sellers of cars and people who rent their caravan/holiday home out
Industry/Entity Type
Advertising
Number of Pages Required
3 page
Colors
Designer to choose colors to be used in the design.
Look and feel

```html
<!DOCTYPE html>
<html lang="en">
<head>
<meta charset="utf-8">
<title>Vanto – Find sellers by code</title>
<link href="https://fonts.googleapis.com/css2?family=Poppins:wght@400;500;600;700;800&family=Roboto:wght@400;500&display=swap" rel="stylesheet">
<style>
:root{
  --yellow:#f5f500;
  --dark:#2f2f2f;
  --black:#000;
  --white:#fff;
  --ink:#1c1c1c;
  --muted:#555;
  --blue:#27a9e8;
  --blue-deep:#1d94d4;
  --line:#cfcfcf;
  --ring:#2aa7e6;
}
*{box-sizing:border-box;margin:0;padding:0}
html,body{width:1200px;height:3030px;overflow:hidden;background:var(--white)}
body{position:relative;font-family:"Roboto",sans-serif;color:var(--ink)}
.abs{position:absolute}
a{color:inherit;text-decoration:none}

/* header / hero */
.hero{position:absolute;left:0;top:0;width:1200px;height:667px;background:var(--dark)}
.brand{position:absolute;display:flex;align-items:center;gap:14px;font-family:"Poppins",sans-serif;font-weight:600;color:var(--yellow);letter-spacing:10px}
.brand-dot{width:30px;height:30px;border-radius:50%;background:var(--yellow)}
.brand--top{left:99px;top:30px;font-size:40px}
.nav{position:absolute;top:45px;font-family:"Roboto",sans-serif;font-size:14px;color:var(--white);letter-spacing:.3px}
.btn-login{position:absolute;left:986px;top:28px;width:114px;height:52px;border-radius:26px;background:var(--yellow);font-family:"Poppins",sans-serif;font-weight:700;font-size:15px;color:var(--ink);display:flex;align-items:center;justify-content:center}
.hero-kicker{position:absolute;left:145px;top:162px;font-family:"Poppins",sans-serif;font-size:23px;color:var(--white)}
.hero-title{position:absolute;left:142px;top:200px;font-family:"Poppins",sans-serif;font-weight:500;font-size:74px;line-height:1;color:var(--white)}
.code-select{position:absolute;top:312px;width:86px;height:60px;border:2px solid var(--yellow);display:flex;align-items:center;justify-content:center;gap:14px;font-family:"Poppins",sans-serif;font-size:36px;color:var(--white)}
.search{position:absolute;left:142px;top:403px;width:237px;height:55px;border:2px solid var(--yellow);border-radius:28px;display:flex;align-items:center;padding-left:24px;font-family:"Poppins",sans-serif;font-weight:600;font-size:15px;color:var(--white);gap:10px}
.search-btn{position:absolute;right:3px;top:3px;width:45px;height:45px;border-radius:50%;background:var(--yellow);display:flex;align-items:center;justify-content:center}
.hero-visual{position:absolute;left:565px;top:94px;width:635px;height:447px;border-radius:48% 40% 46% 38%;background:radial-gradient(ellipse at 45% 55%,#5a5a2a 0%,#45452a 45%,rgba(47,47,47,0) 75%)}
.badge{position:absolute;width:44px;height:44px;border-radius:50%;background:var(--yellow);font-family:"Poppins",sans-serif;font-weight:600;font-size:15px;color:var(--ink);display:flex;align-items:center;justify-content:center}
.dots{position:absolute;display:flex;gap:8px}
.dots span{width:12px;height:12px;border-radius:50%;background:var(--white)}
.dots span.on{background:var(--yellow)}

/* features */
.features{position:absolute;left:98px;top:556px;width:1004px;height:325px;background:var(--white);border-radius:18px;box-shadow:0 6px 24px rgba(0,0,0,.08)}
.feature{position:absolute;top:64px;width:260px;text-align:center}
.feature-icon{width:102px;height:102px;margin:0 auto;border:2px solid var(--ring);border-radius:50%;display:flex;align-items:center;justify-content:center}
.feature h3{margin-top:20px;font-family:"Poppins",sans-serif;font-weight:600;font-size:18px;color:var(--ink)}
.feature p{margin-top:14px;font-size:13.5px;line-height:22px;color:#333}

/* about */
.about-visual{position:absolute;left:127px;top:1009px;width:421px;height:488px;border-radius:46% 54% 40% 60% / 50% 42% 58% 50%;background:linear-gradient(160deg,#c9d3dc 0%,#a9b0b6 40%,#8a7d66 75%,#a8916c 100%)}
.about-title{position:absolute;left:599px;top:992px;font-family:"Poppins",sans-serif;font-weight:700;font-size:37px;color:var(--ink)}
.about-copy{position:absolute;left:599px;width:469px;font-family:"Poppins",sans-serif;font-size:14.5px;line-height:27px;color:#444;text-align:justify}
.btn-yellow{position:absolute;background:var(--yellow);border-radius:28px;display:flex;align-items:center;justify-content:center;color:var(--ink)}
.btn-learn{left:599px;top:1416px;width:143px;height:52px;font-family:"Poppins",sans-serif;font-weight:700;font-size:14.5px}

/* testimonials */
.testimonials{position:absolute;left:0;top:1588px;width:1200px;height:488px;background:linear-gradient(90deg,#2aa2dc 0%,var(--blue) 55%,#2db2ec 100%)}
.section-title{position:absolute;left:0;width:1200px;text-align:center;font-family:"Poppins",sans-serif;font-weight:700;font-size:37px}
.avatar{position:absolute;left:193px;top:1799px;width:148px;height:148px;border-radius:50%;border:3px solid var(--white);padding:6px}
.avatar div{width:100%;height:100%;border-radius:50%;background:linear-gradient(180deg,#c7c7c7 0%,#a58a6c 60%,#d8c3a4 100%)}
.quote-text{position:absolute;left:445px;top:1805px;width:570px;font-family:"Roboto",sans-serif;font-size:15px;line-height:24.5px;color:var(--white)}
.quote-name{position:absolute;left:443px;top:1900px;font-family:"Roboto",sans-serif;font-weight:500;font-size:18px;color:var(--white)}
.quote-role{position:absolute;left:443px;top:1931px;font-size:13px;color:var(--white)}

/* contact */
.field{position:absolute;height:60px;border:1px solid var(--line);border-radius:30px;box-shadow:0 2px 6px rgba(0,0,0,.12);display:flex;align-items:center;padding-left:27px;font-family:"Roboto",sans-serif;font-size:15px;color:#666;background:var(--white)}
.btn-submit{left:513px;top:2546px;width:173px;height:57px;font-family:"Roboto",sans-serif;font-size:17px}

/* footer */
.footer{position:absolute;left:0;top:2723px;width:1200px;height:307px;background:var(--black)}
.brand--foot{left:484px;top:2789px;font-size:44px}
.foot-nav{position:absolute;top:2869px;font-size:14px;color:var(--white)}
.social{position:absolute;top:2920px;width:31px;height:31px;border:1.5px solid var(--white);border-radius:50%}
.copyright{position:absolute;left:0;top:2972px;width:1200px;text-align:center;font-family:"Poppins",sans-serif;font-size:14px;color:var(--white)}
</style>
</head>
<body>

<header class="hero">
  <div class="brand brand--top"><span class="brand-dot"></span>VANTO</div>
  <a class="nav" style="left:554px">HOME</a>
  <a class="nav" style="left:640px">ADVERTISE</a>
  <a class="nav" style="left:759px">CONTACT</a>
  <a class="nav" style="left:862px">REGISTER</a>
  <a class="btn-login">LOG IN</a>

  <p class="hero-kicker">WELCOME TO</p>
  <h1 class="hero-title">VANTO</h1>

  <div class="code-select" style="left:143px">A
    <svg width="14" height="22" viewBox="0 0 14 22"><path d="M7 1 13 9H1Z M7 21 1 13H13Z" fill="#fff"/></svg>
  </div>
  <div class="code-select" style="left:249px">1
    <svg width="14" height="22" viewBox="0 0 14 22"><path d="M7 1 13 9H1Z M7 21 1 13H13Z" fill="#fff"/></svg>
  </div>

  <div class="search">CAR
    <svg width="12" height="8" viewBox="0 0 12 8"><path d="M1 1 6 6 11 1" fill="none" stroke="#fff" stroke-width="2"/></svg>
    <span class="search-btn">
      <svg width="14" height="14" viewBox="0 0 14 14"><circle cx="6" cy="6" r="4.2" fill="none" stroke="#1c1c1c" stroke-width="2"/><path d="M9 9 13 13" stroke="#1c1c1c" stroke-width="2.4"/></svg>
    </span>
  </div>

  <div class="hero-visual" role="img" aria-label="Photo collage of an SUV, a static caravan and a van on a dark splash shape"></div>
  <svg class="abs" style="left:624px;top:166px" width="100" height="64" viewBox="0 0 100 64"><path d="M4 60 Q40 18 90 14" fill="none" stroke="#f5f500" stroke-width="4" stroke-linecap="round"/><path d="M76 4 92 14 78 24" fill="none" stroke="#f5f500" stroke-width="4" stroke-linecap="round" stroke-linejoin="round"/></svg>
  <svg class="abs" style="left:1004px;top:180px" width="100" height="64" viewBox="0 0 100 64"><path d="M96 60 Q64 18 10 16" fill="none" stroke="#f5f500" stroke-width="4" stroke-linecap="round"/><path d="M22 4 8 16 22 28" fill="none" stroke="#f5f500" stroke-width="4" stroke-linecap="round" stroke-linejoin="round"/></svg>
  <span class="badge" style="left:600px;top:272px">X3</span>
  <span class="badge" style="left:829px;top:164px">A8</span>
  <span class="badge" style="left:1097px;top:285px">F7</span>

  <div class="dots" style="left:573px;top:508px"><span></span><span class="on"></span><span></span></div>
</header>

<section class="features">
  <div class="feature" style="left:52px">
    <div class="feature-icon">
      <svg width="50" height="40" viewBox="0 0 50 40"><rect x="3" y="8" width="38" height="24" rx="3" fill="none" stroke="#f5f500" stroke-width="2.5"/><rect x="8" y="12" width="20" height="14" fill="none" stroke="#f5f500" stroke-width="2"/><path d="M41 14H47V26H41 M36 4V8 M36 32V36" fill="none" stroke="#f5f500" stroke-width="2.5"/></svg>
    </div>
    <h3>Simple</h3>
    <p>create&nbsp; your advert and display<br>your code</p>
  </div>
  <svg class="abs" style="left:306px;top:112px" width="90" height="30" viewBox="0 0 90 30"><path d="M2 6 Q40 36 84 8" fill="none" stroke="#555" stroke-width="1.5"/><path d="M76 6 85 7 82 15" fill="none" stroke="#555" stroke-width="1.5"/></svg>
  <div class="feature" style="left:372px">
    <div class="feature-icon">
      <svg width="50" height="56" viewBox="0 0 50 56"><circle cx="28" cy="12" r="7" fill="none" stroke="#f5f500" stroke-width="2.5"/><path d="M16 32Q18 21 28 21Q38 21 40 32" fill="none" stroke="#f5f500" stroke-width="2.5"/><circle cx="22" cy="34" r="9" fill="none" stroke="#f5f500" stroke-width="2.5"/><path d="M15 41 5 52" stroke="#f5f500" stroke-width="3"/></svg>
    </div>
    <h3>Unique</h3>
    <p>customers find you by an easy-to-re-<br>member code</p>
  </div>
  <svg class="abs" style="left:612px;top:100px" width="90" height="30" viewBox="0 0 90 30"><path d="M2 24 Q42 -6 84 22" fill="none" stroke="#555" stroke-width="1.5"/><path d="M77 14 85 22 76 24" fill="none" stroke="#555" stroke-width="1.5"/></svg>
  <div class="feature" style="left:691px">
    <div class="feature-icon">
      <svg width="44" height="54" viewBox="0 0 44 54"><rect x="4" y="4" width="34" height="46" rx="2" fill="none" stroke="#f5f500" stroke-width="2.5"/><g stroke="#f5f500" stroke-width="2"><circle cx="11" cy="14" r="2" fill="none"/><path d="M16 14H32"/><circle cx="11" cy="22" r="2" fill="none"/><path d="M16 22H32"/><circle cx="11" cy="30" r="2" fill="none"/><path d="M16 30H32"/><circle cx="11" cy="38" r="2" fill="none"/><path d="M16 38H32"/></g></svg>
    </div>
    <h3>Effective</h3>
    <p>customers are directed to you and not<br>a list of your competitors</p>
  </div>
</section>

<section class="about">
  <div class="about-visual" role="img" aria-label="Photo of a silver hatchback parked on a roadside, cut into a splash shape"></div>
  <h2 class="about-title">ABOUT VANTO</h2>
  <p class="about-copy" style="top:1068px">Lorem ipsum dolor sit amet, consectetur adipiscing elit, sed do eiusmod tempor incididunt ut labore et dolore magna aliqua. Ut enim ad minim veniam, quis nostrud exercitation ullamco laboris nisi ut aliquip ex ea commodo consequat. Duis aute irure dolor in reprehenderit in voluptate velit esse cillum dolore eu fugiat nulla pariatur. Excepteur sint occaecat cupidatat non proident, sunt in culpa qui officia deserunt mollit anim id est laborum.</p>
  <p class="about-copy" style="top:1276px">Lorem ipsum dolor sit amet, consectetur adipiscing elit, sed do eiusmod tempor incididunt ut labore et dolore magna aliqua. Ut enim ad minim veniam, quis nostrud exercitation ullamco laboris nisi ut aliquip ex ea commodo consequat.</p>
  <a class="btn-yellow btn-learn">LEARN MORE</a>
</section>

<section class="testimonials" role="img" aria-label="Blue-tinted photo of a caravan behind the testimonials"></section>
<h2 class="section-title" style="top:1664px;color:#fff">CLIENT TESTIMONIALS</h2>
<div class="avatar" role="img" aria-label="Portrait photo of a smiling customer"><div></div></div>
<svg class="abs" style="left:444px;top:1771px" width="84" height="16" viewBox="0 0 84 16">
  <g fill="#f7c600"><path id="st" d="M8 0 10.4 5.3 16 5.8 11.8 9.6 13 15.4 8 12.4 3 15.4 4.2 9.6 0 5.8 5.6 5.3Z"/><use href="#st" x="17"/><use href="#st" x="34"/><use href="#st" x="51"/><use href="#st" x="68"/></g>
</svg>
<svg class="abs" style="left:388px;top:1803px" width="38" height="32" viewBox="0 0 38 32"><g fill="#fff" opacity=".35"><path d="M2 32V18Q2 4 16 0V6Q9 9 9 16H16V32Z"/><path d="M21 32V18Q21 4 35 0V6Q28 9 28 16H35V32Z"/></g></svg>
<p class="quote-text">Lorem ipsum dolor sit amet, consectetur adipiscing elit, sed do eiusmod tempor incididunt ut labore et dolore magna aliqua. Ut enim ad minim veniam, quis nostrud exercitation ullamco laboris nisi ut aliquip ex ea commodo consequat.</p>
<p class="quote-name">Marcus</p>
<p class="quote-role">Lorem ipsum dolor</p>
<div class="dots" style="left:443px;top:1979px;gap:5px"><span style="width:11px;height:11px"></span><span class="on" style="width:11px;height:11px"></span><span style="width:11px;height:11px"></span><span style="width:11px;height:11px"></span></div>

<section class="contact">
  <h2 class="section-title" style="top:2186px;color:var(--ink)">CONTACT US</h2>
  <div class="field" style="left:154px;top:2279px;width:436px">First Name :</div>
  <div class="field" style="left:609px;top:2279px;width:436px">Last Name :</div>
  <div class="field" style="left:154px;top:2361px;width:436px">Email :</div>
  <div class="field" style="left:609px;top:2361px;width:436px">Phone :</div>
  <div class="field" style="left:154px;top:2448px;width:890px">Message :</div>
  <a class="btn-yellow btn-submit">SUBMIT</a>
</section>

<footer class="footer"></footer>
<div class="brand brand--foot"><span class="brand-dot" style="width:34px;height:34px"></span>VANTO</div>
<a class="foot-nav" style="left:406px">HOME</a>
<a class="foot-nav" style="left:495px">ADVERTISE</a>
<a class="foot-nav" style="left:620px">CONTACT</a>
<a class="foot-nav" style="left:730px">REGISTER</a>
<a class="social" style="left:510px" aria-label="Social link 1"></a>
<a class="social" style="left:548px" aria-label="Social link 2"></a>
<a class="social" style="left:585px" aria-label="Social link 3"></a>
<a class="social" style="left:623px" aria-label="Social link 4"></a>
<a class="social" style="left:660px" aria-label="Social link 5"></a>
<p class="copyright">©Copyrights 2023 Vanto &nbsp;&nbsp;|&nbsp;&nbsp; All Rights Reserved</p>

</body>
</html>
```